Website for a high end London wedding DJ company

I want a website that is fairly basic but modern. It needs to look professional and smooth. I like white and black backgrounds. I am looking for something similar to this: https://www.veltrispin.uk - at the bottom of this page it has ratewharf reviews as well. I mainly use fendly reviews. This would need to be included, or at least some way of showing all my 5 star reviews on the first page, to get peoples attention.
My current website is www.plumandsway.com
My

Coded - Design and coding required

1 page

• A way to display my reviews. Must be modern.
• Must not look cheesy and 8

```html
<!DOCTYPE html>
<html lang="en">
<head>
<meta charset="utf-8">
<title>Plum &amp; Sway — DJ Hire Surrey</title>
<link rel="stylesheet" href="https://fonts.googleapis.com/css2?family=Libre+Baskerville:wght@400;700&family=Playfair+Display:wght@400;700;900&family=Poppins:wght@400;500&display=swap">
<style>
:root{
  --ink:#111;
  --black:#000;
  --white:#fff;
  --grey-band:#f4f4f4;
  --review-band:#f3f0ee;
  --dark-band:#1c1c1c;
  --bottom-bar:#333;
  --muted:#555;
  --star:#e8702a;
  --link-blue:#4a7bd0;
  --social:#e02020;
  --serif:"Libre Baskerville", Georgia, serif;
  --display:"Playfair Display", Georgia, serif;
  --sans:"Poppins", Arial, sans-serif;
}
*{box-sizing:border-box;margin:0;padding:0}
html,body{width:1200px;height:3560px;overflow:hidden}
body{position:relative;font-family:var(--serif);color:var(--ink);background:var(--white)}
section,header,footer{position:absolute;left:0;width:1200px}

/* Hero */
.hero{top:0;height:603px;overflow:hidden}
.hero-photo{position:absolute;inset:0;background:
  radial-gradient(ellipse at 45% 25%, #3c8a2a 0%, #1f4d18 30%, #0c1a0a 65%, #050805 100%)}
.hero-photo::after{content:"";position:absolute;inset:0;background:linear-gradient(to bottom,rgba(0,0,0,.1),rgba(0,0,0,.55))}
.brand{position:absolute;left:42px;top:22px;font-family:var(--display);font-size:27px;color:var(--white)}
.nav{position:absolute;left:661px;top:34px;display:flex;font-family:var(--sans);font-size:10.5px;font-weight:500;color:var(--white);letter-spacing:.2px}
.nav span{padding:0 10px;border-left:1px solid rgba(255,255,255,.8);line-height:12px}
.nav span:first-child{border-left:none;padding-left:0}
.hero-mark{position:absolute;left:470px;top:168px;width:260px;text-align:center;color:var(--white);font-family:var(--display);font-size:26px;border-top:1px solid rgba(255,255,255,.8);border-bottom:1px solid rgba(255,255,255,.8);padding:6px 0}
.hero-title{position:absolute;left:0;width:1200px;top:340px;text-align:center;font-family:var(--display);font-weight:700;font-size:70px;color:var(--white)}
.hero-stars{position:absolute;left:528px;top:443px}
.btn-contact{position:absolute;left:514px;top:492px;width:168px;height:43px;background:var(--white);color:var(--ink);font-family:var(--sans);font-weight:500;font-size:15px;letter-spacing:1px;display:flex;align-items:center;justify-content:center}

/* About */
.about{top:603px;height:471px}
.frame-band{position:absolute;left:236px;width:362px;height:10px;background:#bdbdbd}
.frame{position:absolute;left:231px;top:100px;width:370px;height:282px;border-left:2px solid #999;border-right:2px solid #999}
.about-photo{position:absolute;left:244px;top:106px;width:343px;height:273px;background:
  radial-gradient(ellipse at 60% 20%, #b04fd8 0%, #5d2a7a 30%, #26122f 70%, #140a18 100%)}
.about-text{position:absolute;left:675px;top:70px;width:310px}
.about-text h1{font-family:var(--display);font-weight:700;font-size:46px;line-height:1}
.about-text h2{font-family:var(--serif);font-weight:400;font-size:25px;color:#333;margin-top:8px}
.about-text p{font-size:10.5px;line-height:16.5px;margin-top:20px;color:#222}
.about-text p+p{margin-top:16px}
.btn-book{display:inline-block;margin-top:30px;background:var(--black);color:var(--white);font-size:11.5px;padding:8px 18px}

/* Section heads */
.section-head{position:absolute;left:0;width:1200px;text-align:center}
.section-head h2{font-family:var(--serif);font-weight:400;font-size:35px}
.section-head p{font-size:10px;margin-top:6px;color:#222}

/* Services */
.services{top:1074px;height:516px;background:var(--grey-band)}
.card{position:absolute;overflow:hidden}
.card .photo{position:absolute;inset:0}
.card .label{position:absolute;left:0;right:0;bottom:0;background:var(--black);color:var(--white);font-family:var(--display);font-weight:900;font-size:22px;padding-left:18px;display:flex;align-items:center}
.card .overline{position:absolute;left:10px;font-size:10px;color:var(--white);line-height:15px}

/* Why */
.why{top:1590px;height:442px;overflow:hidden}
.why-photo{position:absolute;inset:0;background:
  radial-gradient(ellipse at 40% 20%, #7a4a8a 0%, #4a2d4a 35%, #2a1c1c 70%, #1a1210 100%)}
.why-photo::after{content:"";position:absolute;inset:0;background:rgba(0,0,0,.35)}
.why h2{position:absolute;left:0;width:1200px;top:150px;text-align:center;font-size:31px;font-weight:400;color:var(--white)}
.why p{position:absolute;left:290px;width:620px;top:235px;text-align:center;color:var(--white);font-size:15.5px;line-height:22.5px}

/* DJs */
.djs{top:2032px;height:404px}
.card.explore{background:var(--black);color:var(--white);font-family:var(--display);font-weight:900;font-size:23px;text-align:center;line-height:30px;display:flex;align-items:center;justify-content:center;padding-bottom:40px}

/* Reviews */
.reviews{top:2436px;height:426px;background:var(--review-band)}
.reviews h2{font-family:var(--serif);font-weight:700;font-size:33px}
.review{position:absolute;top:145px;width:189px;height:108px;background:#fafafa;padding:10px 10px 0 24px;font-family:var(--sans);font-size:7.5px;line-height:12.5px;color:#888}
.review .quote{position:absolute;left:6px;top:2px;font-size:20px;color:#ccc;font-family:var(--serif)}
.review .stars{display:inline-block;vertical-align:-1px;margin-right:4px}
.review .mark{position:absolute;right:6px;bottom:6px;width:10px;height:10px;border-radius:50%;border:2px solid #5b8ff0}
.review u{color:var(--link-blue)}
.reviewer{position:absolute;top:268px;display:flex;gap:8px;font-family:var(--sans);font-size:8.5px}
.reviewer .avatar{width:28px;height:28px;border-radius:50%;background:#555}
.reviewer b{color:var(--link-blue);font-weight:500;display:block;margin-top:2px}
.reviewer small{color:#aaa;font-size:7px}
.arrow{position:absolute;top:218px;font-family:var(--sans);font-size:12px;color:#999}
.dots{position:absolute;left:568px;top:316px;display:flex;gap:6px}
.dots i{width:4px;height:4px;border-radius:50%;background:#ccc}
.dots i:first-child{background:var(--link-blue)}
.rating-badge{position:absolute;left:538px;top:353px;width:123px;height:40px;background:var(--white);border-top:3px solid #4caf50;box-shadow:0 1px 3px rgba(0,0,0,.2);display:flex;align-items:center;gap:6px;padding-left:8px;font-family:var(--sans)}
.rating-badge .dot{width:20px;height:20px;border-radius:50%;border:3px solid #888}
.rating-badge small{display:block;font-size:7px;color:#555}
.rating-badge b{font-weight:400;font-size:11px;color:var(--star)}

/* Contact */
.contact{top:2862px;height:456px;background:var(--dark-band);color:var(--white)}
.contact h2{font-family:var(--serif);font-weight:700;font-size:25px}
.contact .lede{font-size:10.5px;margin-top:18px;color:var(--white)}
.contact .areas{font-size:10.5px;font-weight:700;margin-top:8px;color:var(--white)}
.field{position:absolute;background:var(--white);color:#666;font-family:var(--sans);font-size:11.5px;padding:0 18px;display:flex;align-items:center}
.field.area{align-items:flex-start;padding-top:14px;padding-left:12px}
.btn-submit{position:absolute;left:480px;top:374px;width:239px;height:42px;background:var(--white);color:var(--ink);font-size:12px;display:flex;align-items:center;justify-content:center}

/* Footer */
.site-footer{top:3318px;height:200px}
.footer-brand{position:absolute;left:220px;top:30px;font-family:var(--display);font-size:18px;border-top:1px solid #555;border-bottom:1px solid #555;padding:2px 24px}
.footer-about{position:absolute;left:214px;top:82px;width:255px;font-size:9.5px;line-height:15px;color:#333}
.col{position:absolute;top:68px;font-size:9.5px;line-height:19px;color:#333}
.col h4{font-family:var(--sans);font-weight:500;font-size:10px;color:#222;margin-bottom:5px}
.col .addr{font-size:8.5px;line-height:13px;display:block}
.follow{position:absolute;left:823px;top:126px;font-family:var(--sans);font-size:10px;color:var(--social)}
.socials{position:absolute;left:823px;top:150px;display:flex;gap:5px}
.socials i{width:18px;height:18px;border-radius:50%;background:var(--social)}
.bottom-bar{top:3518px;height:42px;background:var(--bottom-bar);color:#ddd;font-size:9.5px}
.bottom-bar .copy{position:absolute;left:216px;top:16px}
.bottom-bar .legal{position:absolute;left:763px;top:16px}
</style>
</head>
<body>
<svg width="0" height="0" style="position:absolute">
  <defs>
    <symbol id="star" viewBox="0 0 24 24"><path d="M12 2l2.9 6.9 7.1.6-5.4 4.7 1.6 7L12 17.5 5.8 21.2l1.6-7L2 9.5l7.1-.6z"/></symbol>
  </defs>
</svg>

<header class="hero">
  <div class="hero-photo" role="img" aria-label="Crowd dancing under green stage lasers at a club night"></div>
  <div class="brand">Plum &amp; Sway</div>
  <nav class="nav"><span>DJ</span><span>MUSICIAN</span><span>EVENT PRODUCTION</span><span>GALLERY</span><span>NEWS</span><span>CONTACT</span><span>LOGIN</span></nav>
  <div class="hero-mark">Plum &amp; Sway</div>
  <div class="hero-title">Plum &amp; Sway</div>
  <svg class="hero-stars" width="144" height="22" fill="none" stroke="#fff" stroke-width="1.6">
    <use href="#star" x="0" width="22" height="22"/><use href="#star" x="30" width="22" height="22"/><use href="#star" x="60" width="22" height="22"/><use href="#star" x="90" width="22" height="22"/><use href="#star" x="120" width="22" height="22"/>
  </svg>
  <div class="btn-contact">CONTACT US</div>
</header>

<section class="about">
  <div class="frame-band" style="top:82px" role="img" aria-label="Decorative scroll border"></div>
  <div class="frame"></div>
  <div class="about-photo" role="img" aria-label="Bride and guests dancing under purple lights at a wedding reception"></div>
  <div class="frame-band" style="top:387px" role="img" aria-label="Decorative scroll border"></div>
  <div class="about-text">
    <h1>DJ</h1>
    <h2>Hire Surrey</h2>
    <p>Welcome to Plum and Sway DJ hire Surrey. With 100% 5 star reviews on Fendly, having only started in September 2019, we are fast becoming the number 1 DJ hire company in Surrey.</p>
    <p>Whether you are looking to book for weddings, birthday parties or any occasion full of sparkle and dancing, our London and Surrey wedding DJ provides a bespoke 5 star service, guaranteed to make you want to dance.</p>
    <span class="btn-book">Book Now</span>
  </div>
</section>

<section class="services">
  <div class="section-head" style="top:30px"><h2>DJ SERVICES</h2><p>Checkout our various services</p></div>
  <div class="card" style="left:200px;top:130px;width:250px;height:300px">
    <div class="photo" role="img" aria-label="DJ in a white shirt mixing at a rustic venue" style="background:linear-gradient(160deg,#9b8a6a,#5b4a34 60%,#2b2218)"></div>
    <div class="overline" style="top:214px">WEDDING DJ, CORPORATE DJ,<br>CLUB DJ &amp; MORE..</div>
    <div class="label" style="height:50px">DJ’s</div>
  </div>
  <div class="card" style="left:474px;top:130px;width:250px;height:300px">
    <div class="photo" role="img" aria-label="Stage lighting fixtures glowing blue and purple" style="background:linear-gradient(180deg,#c8b6a4,#9a7f6c 55%,#5a3e3a)"></div>
    <div class="label" style="height:50px">Event Production</div>
  </div>
  <div class="card" style="left:748px;top:130px;width:250px;height:300px">
    <div class="photo" role="img" aria-label="Guitarist performing on a stage with purple lighting" style="background:radial-gradient(ellipse at 40% 40%,#c040d0,#5a1f70 45%,#1a0a22)"></div>
    <div class="label" style="height:50px">DJ &amp; Musician</div>
  </div>
</section>

<section class="why">
  <div class="why-photo" role="img" aria-label="Wedding guests dancing together on a crowded dance floor"></div>
  <h2>WHY CHOOSE US?</h2>
  <p>With 13 years of experience in the DJing industry, we take care of the finer details to make planning your wedding day or special celebration a smooth and enjoy-able experience.</p>
</section>

<section class="djs">
  <div class="section-head" style="top:56px"><h2>OUR DJs</h2><p>Explore our dj profiles and crews</p></div>
  <div class="card" style="left:200px;top:152px;width:187px;height:220px">
    <div class="photo" role="img" aria-label="DJ portrait at the decks" style="background:linear-gradient(160deg,#9b8a6a,#5b4a34 60%,#2b2218)"></div>
    <div class="label" style="height:51px">DJ Plum</div>
  </div>
  <div class="card" style="left:404px;top:152px;width:186px;height:220px">
    <div class="photo" role="img" aria-label="DJ mixing on a controller" style="background:linear-gradient(150deg,#4a4a52,#2a2a30 50%,#8a8078)"></div>
    <div class="label" style="height:51px">DJ Plum</div>
  </div>
  <div class="card" style="left:608px;top:152px;width:187px;height:220px">
    <div class="photo" role="img" aria-label="DJ under smoky stage lights" style="background:radial-gradient(ellipse at 70% 20%,#8a9aa6,#3a4450 40%,#12161a)"></div>
    <div class="label" style="height:51px">DJ Plum</div>
  </div>
  <div class="card explore" style="left:812px;top:152px;width:186px;height:220px">Explore<br>More<br>DJ</div>
</section>

<section class="reviews">
  <div class="section-head" style="top:42px"><h2>Fendly Reviews</h2><p style="margin-top:18px">Checkout our fendly reviews</p></div>
  <span class="arrow" style="left:274px">‹</span>
  <div class="review" style="left:289px"><span class="quote">“</span>
    <svg class="stars" width="60" height="9" fill="var(--star)"><use href="#star" width="9" height="9"/><use href="#star" x="12" width="9" height="9"/><use href="#star" x="24" width="9" height="9"/><use href="#star" x="36" width="9" height="9"/><use href="#star" x="48" width="9" height="9"/></svg>Best in the business. Took a long time to find these guys and im not letting them go anytime soon.<i class="mark"></i></div>
  <div class="review" style="left:506px"><span class="quote">“</span>
    <svg class="stars" width="60" height="9" fill="var(--star)"><use href="#star" width="9" height="9"/><use href="#star" x="12" width="9" height="9"/><use href="#star" x="24" width="9" height="9"/><use href="#star" x="36" width="9" height="9"/><use href="#star" x="48" width="9" height="9"/></svg>Rob and our account manager, Declan, have done a great job assessing our accounts and managing them accordingly. We have a relatively difficult account to mange and their approach in doing so is <u>read more</u><i class="mark"></i></div>
  <div class="review" style="left:723px"><span class="quote">“</span>
    <svg class="stars" width="60" height="9" fill="var(--star)"><use href="#star" width="9" height="9"/><use href="#star" x="12" width="9" height="9"/><use href="#star" x="24" width="9" height="9"/><use href="#star" x="36" width="9" height="9"/><use href="#star" x="48" width="9" height="9"/></svg>Professional and expert, time-thoughtful, client-minded. It's been pleasure and I am looking forward to our continued and growing relationship.<i class="mark"></i></div>
  <span class="arrow" style="left:923px">›</span>
  <div class="reviewer" style="left:299px"><i class="avatar" style="background:#222"></i><div><b>The Velvet Hours</b><small>4 days ago</small></div></div>
  <div class="reviewer" style="left:515px"><i class="avatar" style="background:#8a6a50"></i><div><b>Nadia Hollis</b><small>4 months ago</small></div></div>
  <div class="reviewer" style="left:732px"><i class="avatar" style="background:#444"></i><div><b>Owen Tarrant</b><small>4 months ago</small></div></div>
  <div class="dots"><i></i><i></i><i></i><i></i><i></i><i></i><i></i></div>
  <div class="rating-badge"><i class="dot"></i><div><small>Fendly Rating</small><b>5.0 ★★★★★</b></div></div>
</section>

<section class="contact">
  <div class="section-head" style="top:34px">
    <h2>Surrey’s Number 1 DJ Service</h2>
    <p class="lede">We are quite literally, UNBEATABLE. So if you are looking for the best DJ in London and Surrey, get in touch.</p>
    <p class="areas">Wedding DJ London &nbsp;|&nbsp; Wedding DJ Surrey &nbsp;|&nbsp; Party DJ London &nbsp;|&nbsp; DJ Kingston</p>
  </div>
  <div class="field" style="left:292px;top:177px;width:293px;height:43px">your name</div>
  <div class="field" style="left:611px;top:177px;width:293px;height:43px">enter your email id</div>
  <div class="field area" style="left:292px;top:238px;width:612px;height:118px">your requirement</div>
  <div class="btn-submit">Submit Your Message</div>
</section>

<footer class="site-footer">
  <div class="footer-brand">Plum &amp; Sway</div>
  <p class="footer-about">With experience of working with many popular wedding and party venues across London and Surrey, we work in partnership with venues, wedding planners, bands, musicians and other companies to ensure your big day is exactly as you want it.</p>
  <div class="col" style="left:494px"><h4>Quick Links</h4>Home<br>About<br>Services<br>Contact</div>
  <div class="col" style="left:599px"><h4>Contact Info</h4>Ph: 07700 900318<br>Email: info@plumandsway.com</div>
  <div class="col" style="left:823px"><h4>Office Location</h4><span class="addr">18 LARKMOOR ROW, COVENT<br>GARDEN, LONDON, WC2X 4QP</span></div>
  <div class="follow">Follow Us</div>
  <div class="socials"><i></i><i></i><i></i><i></i><i></i></div>
</footer>
<section class="bottom-bar">
  <span class="copy">Copyright © 2021, All rights reserved, Plum &amp; Sway</span>
  <span class="legal">Privacy Policy &nbsp;|&nbsp; Sitemap &nbsp;|&nbsp; Terms And Conditions</span>
</section>
</body>
</html>
```